Regenerative Medicine Brochure

I want a clean modern bi-fold or tri-fold brochure. We offer non-surgical joint repair for knees, shoulders, and hips. We have many services available including regenerative medicine including stem cell allograft, palatelet rich plasma, prolotherapy, triggerpoint injection, chiropractic and rehab therapies. We are a modern multidisciplinary clinic in coastal California. My logo is already complete and is a vibrant green color. I prefer lots of white space with some areas for service description and what conditions may benefit from the services. Design should convey modern treatments, upscale office and practice, and our target audience is older adults who want to maintain an active pain-free lifestyle.

Target Market(s)

Sports injuries, athletes, seniors who are active, knee pain, shoulder pain, arthritis.

Industry/Entity Type

Alternative Medicine

Font styles to use
Serif

Colors
9bcb3c

Requirements
Must have
• Small white space where we can write date, time, location of next event/class. Colors in brochure to coordinate with logo colors provided.

```html
<!DOCTYPE html>
<html lang="en">
<head>
<meta charset="utf-8">
<title>Coastline Spine &amp; Joint – Regenerative Medicine Brochure</title>
<link href="https://fonts.googleapis.com/css2?family=Hind:wght@300;400;500;600&display=swap" rel="stylesheet">
<style>
:root{
  --backdrop:#d5d6da;
  --green:#4bb748;
  --green-soft:#8fd18a;
  --heading-green:#47b04a;
  --band:#a9bfcd;
  --text:#4f5458;
  --dark:#222;
  --white:#fff;
  --slate:#6f8592;
}
*{margin:0;padding:0;box-sizing:border-box}
html,body{width:889px;height:1200px;overflow:hidden}
body{background:var(--backdrop);font-family:"Hind",Arial,sans-serif;color:var(--text);position:relative}
.spread{position:absolute;left:122px;width:656px;height:510px;background:var(--white);box-shadow:0 10px 14px -6px rgba(0,0,0,.35)}
.spread--outside{top:54px}
.spread--inside{top:616px}
.panel{position:absolute;top:0;height:510px;overflow:hidden}
.panel--left{left:0;width:214px;background:var(--white)}
.panel--mid{left:214px;width:216px;background:var(--green);color:var(--white)}
.panel--right{left:430px;width:226px;background:var(--white)}
.photo{position:absolute;left:0;width:100%}
.photo svg{display:block;width:100%;height:100%}
.heading{position:absolute;left:12px;right:10px;color:var(--heading-green);font-weight:600;font-size:11px;line-height:10.5px}
.rule{position:absolute;height:1px;background:#c9d3d9}
.body-text{position:absolute;left:12px;right:10px;font-size:8.6px;line-height:10.6px;text-align:justify;font-weight:400}
.body-text p+p{margin-top:10.6px}
.mid-text{position:absolute;left:18px;right:18px;font-size:8.5px;line-height:9.9px;text-align:center}
.clinic-name{position:absolute;left:0;right:0;text-align:center;font-weight:600;font-size:14px;line-height:15px;color:var(--white)}
.phone{position:absolute;display:flex;align-items:center;gap:9px;font-weight:500;letter-spacing:1px}
.phone svg{width:13px;height:13px}
.event-field{position:absolute;left:15px;width:187px;height:13px;border-radius:3px;background:var(--green-soft);font-size:5.5px;line-height:13px;padding-left:5px;color:var(--white)}
.address{position:absolute;left:0;right:0;text-align:center;font-size:10.5px;line-height:11.8px;font-weight:300}
.band{position:absolute;height:20px;background:var(--band);color:var(--white)}
.map{position:absolute;left:48px;top:24px;width:118px;height:118px;border-radius:50%;border:6px solid #d9ecd3;background:#eef1ee}
.brand-line{position:absolute;left:14px;top:38px;display:flex;align-items:center;gap:8px}
.brand-line .mark{width:10px;height:10px;background:var(--green)}
.brand-line .name{font-size:16px;font-weight:600;color:var(--dark)}
.tagline{position:absolute;left:0;right:0;text-align:center}
.area-grid{position:absolute;left:0;top:126px;width:216px}
.area{position:absolute;width:60px;text-align:center;font-size:8.5px}
.area span.icon{display:block;width:50px;height:50px;margin:0 auto 4px;border-radius:50%;border:2px solid #dfe9f5;background:radial-gradient(circle at 50% 45%,#f2664a 0,#7a3aa0 30%,#1d3a8c 70%,#0e1f55 100%)}
</style>
</head>
<body>

<section class="spread spread--outside">

  <div class="panel panel--left">
    <div class="photo" style="top:0;height:165px" role="img" aria-label="Photo of a doctor at a desk with a laptop and stethoscope">
      <svg viewBox="0 0 214 165" preserveAspectRatio="none">
        <defs><linearGradient id="deskTone" x1="0" y1="0" x2="1" y2="1"><stop offset="0" stop-color="#3e5168"/><stop offset=".55" stop-color="#8ea3b8"/><stop offset="1" stop-color="#e3e8ee"/></linearGradient></defs>
        <path d="M0 0H214V150Q110 140 0 160Z" fill="url(#deskTone)"/>
        <path d="M0 160Q110 140 214 150" fill="none" stroke="#e3e6e8" stroke-width="3"/>
      </svg>
    </div>
    <h2 class="heading" style="top:169px">What can I expect from regenerative medicine treatments?</h2>
    <div class="rule" style="left:12px;top:197px;width:78px"></div>
    <div class="body-text" style="top:203px">
      <p>During your visit, the team begins with a consultation and physical exam to determine if you’re a candidate for regenerative medicine. They ask about your symptoms, condition, overall health, and lifestyle. If you’re a candidate, the team then explains the procedure and what to expect both during and afterward.</p>
      <p>For the procedure, the team first cleans your skin and applies a topical numbing cream to your skin, if needed. Next, the team injects regenerative products into the treatment area. You may feel a slight pinch or burning sensation during the injection. The injection takes less than five minutes and you can return to your usual activities the same day. Mild soreness at the injection site is possible for two to three days.</p>
      <p>Over the coming weeks and months, the injected products help repair damaged tissues at the treatment site. Most people notice results after two months. Follow-up care may be recommended based on your condition and initial results. The team has seen dramatic results with regenerative medicine treatments, however, individual results can vary. Speak to the team to see if regenerative medicine is right for you.</p>
    </div>
  </div>

  <div class="panel panel--mid">
    <div class="map" role="img" aria-label="Street map showing the clinic location"></div>
    <p class="clinic-name" style="top:170px">Coastline Spine &amp; Joint</p>
    <p class="mid-text" style="top:215px">For joint arthritis and muscle pain and injuries, the team at Coastline Spine &amp; Joint offers minimally invasive regenerative medicine techniques to help you recover from chronic pain. Located in Seabright, California, the medical team utilizes advanced restorative techniques to support the natural healing of injured joints and soft tissues without the need for surgery.</p>
    <p class="mid-text" style="top:309px">To learn more, schedule a consultation online or by phone today.</p>
    <div class="phone" style="left:49px;top:338px;font-size:13px">
      <svg viewBox="0 0 24 24"><circle cx="12" cy="12" r="10.5" fill="none" stroke="#fff" stroke-width="1.6"/><path d="M8.6 6.8l1.6-.3 1.2 2.7-1 1c.6 1.3 1.6 2.3 2.9 2.9l1-1 2.7 1.2-.3 1.6c-.2.6-.8 1-1.5.9-3.8-.5-6.8-3.5-7.3-7.3-.1-.7.3-1.3.7-1.7z" fill="#fff"/></svg>
      805-555-0142
    </div>
    <div class="event-field" style="top:373px">next event/class:</div>
    <div class="event-field" style="top:389px">date:</div>
    <div class="event-field" style="top:405px">location:</div>
    <div class="address" style="top:440px">420 Harbor Way<br>Seabright, CA 93400</div>
  </div>

  <div class="panel panel--right">
    <div class="brand-line">
      <span class="mark"></span>
      <span class="name">Coastline Spine &amp; Joint</span>
    </div>
    <div class="photo" style="top:86px;height:306px" role="img" aria-label="Photo of an older couple walking hand in hand on a sunny beach">
      <svg viewBox="0 0 226 306" preserveAspectRatio="none">
        <defs><linearGradient id="beachTone" x1="0" y1="0" x2="0" y2="1"><stop offset="0" stop-color="#c9cfd0"/><stop offset=".35" stop-color="#e9d2a9"/><stop offset=".7" stop-color="#d9a55e"/><stop offset="1" stop-color="#b8783a"/></linearGradient></defs>
        <path d="M0 8Q113 -4 226 6V282Q113 318 0 296Z" fill="url(#beachTone)"/>
        <path d="M0 296Q113 318 226 282" fill="none" stroke="var(--green)" stroke-width="3"/>
      </svg>
    </div>
    <p class="tagline" style="top:427px;font-size:11px;color:var(--slate);font-weight:400">REGENERATIVE MEDICINE SPECIALISTS</p>
    <p class="tagline" style="top:444px;font-size:15px;color:var(--dark);font-weight:600">Regenerative Medicine Q &amp; A</p>
  </div>

  <div class="band" style="left:214px;top:473px;width:442px">
    <span style="position:absolute;left:24px;top:3px;font-size:12px;font-weight:300">www.coastlinespineandjoint.com</span>
    <div class="phone" style="left:265px;top:1px;font-size:12.5px">
      <svg viewBox="0 0 24 24"><circle cx="12" cy="12" r="10.5" fill="none" stroke="#fff" stroke-width="1.6"/><path d="M8.6 6.8l1.6-.3 1.2 2.7-1 1c.6 1.3 1.6 2.3 2.9 2.9l1-1 2.7 1.2-.3 1.6c-.2.6-.8 1-1.5.9-3.8-.5-6.8-3.5-7.3-7.3-.1-.7.3-1.3.7-1.7z" fill="#fff"/></svg>
      805-555-0142
    </div>
  </div>
</section>

<section class="spread spread--inside">

  <div class="panel panel--left" style="width:220px">
    <div class="photo" style="top:0;height:190px" role="img" aria-label="Photo of clinicians reviewing notes with an older patient">
      <svg viewBox="0 0 220 190" preserveAspectRatio="none">
        <defs><linearGradient id="clinicTone" x1="0" y1="0" x2="1" y2="0"><stop offset="0" stop-color="#dfe3e6"/><stop offset=".45" stop-color="#7d9cc6"/><stop offset="1" stop-color="#b9c3cc"/></linearGradient></defs>
        <path d="M0 0H220V184Q110 168 0 186Z" fill="url(#clinicTone)"/>
      </svg>
    </div>
    <h2 class="heading" style="top:218px">What is regenerative medicine?</h2>
    <div class="rule" style="left:12px;top:232px;width:98px"></div>
    <div class="body-text" style="top:240px;right:12px">
      <p>Regenerative medicine is a form of biotechnology that involves injecting regenerative medicine products into injured tissues to help your body repair damage. Regenerative medicine uses tissue engineering techniques to repair muscles, ligaments, cartilage, and tendons damaged by injuries, overuse, and osteoarthritis.</p>
      <p>The medical providers at Coastline Spine &amp; Joint select from a variety of available treatments and products. These include amniotic allografts, hyaluronic acid, regenerative cells, and cytokines which are powerful growth factors that may help regenerate your own body’s tissues.</p>
      <p>After your injection with the amniotic allograft serum, the growth factors trigger repair at the site of injection. Over the course of the next several weeks, cells grow and multiply forming new tissue.</p>
    </div>
  </div>

  <div class="panel panel--mid" style="left:220px;width:216px">
    <p class="clinic-name" style="top:26px">Coastline Spine &amp; Joint</p>
    <p class="mid-text" style="top:76px;left:12px;right:12px;font-size:10px;line-height:10.5px;font-weight:600">Regenerative medicine may be used in the following areas:</p>
    <div class="rule" style="left:18px;top:105px;width:168px;background:#fff"></div>
    <div class="area-grid">
      <div class="area" style="left:8px;top:0"><span class="icon" role="img" aria-label="Shoulder joint illustration"></span>SHOULDER</div>
      <div class="area" style="left:72px;top:0"><span class="icon" role="img" aria-label="Elbow joint illustration"></span>ELBOW</div>
      <div class="area" style="left:136px;top:0"><span class="icon" role="img" aria-label="Wrist joint illustration"></span>WRIST</div>
      <div class="area" style="left:8px;top:77px"><span class="icon" role="img" aria-label="Hip joint illustration"></span>HIP</div>
      <div class="area" style="left:72px;top:77px"><span class="icon" role="img" aria-label="Knee joint illustration"></span>KNEE</div>
      <div class="area" style="left:136px;top:77px"><span class="icon" role="img" aria-label="Ankle joint illustration"></span>ANKLE</div>
    </div>
    <div class="body-text" style="top:296px;left:5px;right:14px;text-align:left;color:#fff">
      <p>There are many additional types of bone and soft tissue problems, including arthritis, that these injections may benefit.</p>
      <p>With regenerative medicine and amniotic allograft treatments, the team supports the natural healing abilities of your body without the need for drugs or surgical repair and painful recovery. However, not all forms of regenerative medicine are equal.</p>
      <p>At Coastline Spine &amp; Joint, the team only works with the best regenerative medicine labs to ensure that the right kind of products are selected and that they are of the best quality and highest safety.</p>
    </div>
  </div>

  <div class="panel panel--right" style="left:436px;width:220px">
    <h2 class="heading" style="top:24px;left:9px">How does regenerative medicine work?</h2>
    <div class="rule" style="left:9px;top:38px;width:95px"></div>
    <div class="body-text" style="top:53px;left:9px;right:14px">
      <p>The team uses lab-grade products that are sterilized and processed to inject into the injured area. Once injected, it is thought that these powerful products differentiate into a variety of tissues to trigger your own body to repair damaged tissues. This damage may involve minor tears in muscles, ligaments, and tendons, or cartilage and meniscus breakdown in joints.</p>
      <p>Regenerative medicine products contain the basic building blocks of the body tissues — including proteins, amino acids, and cytokines — responsible for healing and tissue growth. They also provide anti-inflammatory benefits by promoting repair of tissues affected by inflammation.</p>
      <p>While some inflammation is normal and has a benefit to healing injuries, long-term inflammation causes pain, swelling, and further damage to tissues. When you experience too much inflammation, it does more harm than good. Instead of constantly relying on anti-inflammatory medications, regenerative products may be able to correct the problem at the source and reduce the production of natural inflammatory chemicals so you can heal.</p>
    </div>
    <div class="photo" style="top:330px;height:180px" role="img" aria-label="Photo of a surfer carrying a board out of the ocean at dusk">
      <svg viewBox="0 0 220 180" preserveAspectRatio="none">
        <defs><linearGradient id="surfTone" x1="0" y1="0" x2="0" y2="1"><stop offset="0" stop-color="#e6c3c2"/><stop offset=".3" stop-color="#8e8aa6"/><stop offset=".65" stop-color="#6f7f9a"/><stop offset="1" stop-color="#b3b6c2"/></linearGradient></defs>
        <rect width="220" height="180" fill="url(#surfTone)"/>
      </svg>
    </div>
  </div>

  <div class="band" style="left:0;top:473px;width:436px">
    <span style="position:absolute;left:13px;top:3px;font-size:11.5px;font-weight:300">To learn more, schedule a visit online or by phone at Coastline Spine &amp; Joint now.</span>
  </div>
</section>

</body>
</html>
```